Header for Website

We need a header for our website that includes a simple logo. We will need to be able to seperate out the logo from the header to use on sales and marketing so we will also need this as a seperate file. We run an online sports platfom that covers several geographies and languages.

We need something simple but identifiable. Most of the sports we cover are team sports.

The company objectives are to use their community to crowdfund for projects and provide administration to help clubs run their teams and members.

Reason: I've extended this because of a holiday

Target Market(s)

Our target market will generally be men and women over the age of 40 who like team sports

Industry/Entity Type

Marketing

```html
<!DOCTYPE html>
<html lang="en">
<head>
<meta charset="utf-8">
<title>TeamPool.net – Developing your club together</title>
<link href="https://fonts.googleapis.com/css2?family=Ubuntu:wght@400;500;700&family=Arimo:wght@400&display=swap" rel="stylesheet">
<style>
  :root{
    --navy:#0a0a3a;
    --brand:#1b1f7a;
    --cyan:#00a8e6;
    --purple:#b03bc0;
    --orange:#e98a1f;
    --rust:#c0552a;
    --rust-dark:#a84622;
    --red:#d01818;
    --blue-link:#1f6fb8;
    --banner-blue:#0d5ca3;
    --banner-light:#6aa6d6;
    --footer-bg:#f1f1f1;
    --footer-bar:#242424;
    --text:#111;
  }
  *{box-sizing:border-box;margin:0;padding:0}
  html,body{width:800px;height:1200px;overflow:hidden}
  body{position:relative;background:#fff;font-family:"Ubuntu",sans-serif;color:var(--text)}
  .abs{position:absolute}

  /* header */
  .nav-band{left:0;top:82px;width:800px;height:287px;background:var(--navy)}
  .brand-dot{left:30px;top:28px;width:72px;height:72px;border-radius:50%;background:var(--brand);border:5px solid #fff}
  .brand-name{left:116px;top:27px;font-size:33px;line-height:1;color:var(--brand);white-space:nowrap}
  .brand-tag{left:116px;top:60px;width:268px;text-align:right;font-size:9px;color:var(--brand);white-space:nowrap}
  .main-nav{left:112px;top:82px;height:26px;display:flex}
  .main-nav a{color:#fff;text-decoration:none;font-size:15px;padding:9px 16px 0;border-left:1px solid #fff;height:26px}
  .main-nav a:first-child{border-left:none}

  /* hero */
  .hero-frame{left:22px;top:130px;width:753px;height:278px;background:#fff}
  .hero-photo{left:30px;top:139px;width:737px;height:261px;
    background:linear-gradient(180deg,#3f9b2f 0%,#58b23c 45%,#3d8e2c 100%)}
  .hero-ball{left:380px;top:278px;width:170px;height:122px;border-radius:85px 85px 0 0;
    background:radial-gradient(circle at 50% 60%,#f4f0ea,#c9c2b8 70%,#58b23c 72%)}
  .hero-line1{left:71px;top:208px;font-size:28px;color:#fff;white-space:nowrap}
  .hero-line2{left:71px;top:246px;font-size:25px;color:#111;white-space:nowrap}
  .feature{left:561px;width:199px;padding:14px 0 0 20px;color:#fff}
  .feature h3{font-weight:400;font-size:19px;letter-spacing:.3px;margin-bottom:6px;white-space:nowrap}
  .feature p{font-size:10.5px;line-height:14px;width:170px}
  .f-fund{top:145px;height:82px;background:var(--cyan);border-left:6px solid var(--navy)}
  .f-admin{top:229px;height:80px;background:var(--purple)}
  .f-goods{top:311px;height:81px;background:var(--orange)}
  .f-notch{left:552px;top:180px;width:0;height:0;border:9px solid transparent;border-right-color:var(--navy)}

  /* intro */
  .intro{left:0;width:800px;text-align:center;font-size:18.5px;white-space:nowrap}
  .intro-1{top:426px}
  .intro-2{top:456px}
  .intro-2 .free{color:var(--red);font-size:28px}
  .intro-arrow{left:712px;top:466px}

  /* register section */
  .register{left:0;top:509px;width:800px;height:366px;background:var(--rust);
    background-image:repeating-linear-gradient(45deg,rgba(0,0,0,.04) 0 2px,transparent 2px 6px)}
  .video{left:28px;top:542px;width:412px;height:268px;background:#111}
  .video-still{left:28px;top:566px;width:412px;height:214px;
    background:linear-gradient(160deg,#f2f2f2,#dcdcdc)}
  .video-progress{left:28px;top:780px;width:412px;height:8px;background:#e2231a}
  .video-controls{left:28px;top:788px;width:412px;height:22px;background:#1a1a1a}
  .play{left:46px;top:794px;width:0;height:0;border-left:10px solid #bbb;border-top:6px solid transparent;border-bottom:6px solid transparent}
  .time{left:100px;top:794px;font-size:9px;color:#fff;font-family:"Arimo",sans-serif}
  .form-title{left:472px;top:523px;width:320px;text-align:center;font-size:18px;font-weight:500;color:#fff;white-space:nowrap;line-height:1.2}
  .field{left:497px;width:248px;height:28px;background:#fff;border:2px solid var(--rust-dark);border-radius:5px;
    box-shadow:0 0 0 1px rgba(255,255,255,.5);font-size:12px;color:#555;padding:6px 12px}
  .field-select::after{content:"";position:absolute;right:10px;top:11px;border:5px solid transparent;border-top-color:#d14b1e}
  .help{left:508px;top:787px;font-size:11.5px;color:#fff;white-space:nowrap}
  .cta{left:514px;top:823px;width:210px;height:38px;border-radius:6px;border:2px solid var(--rust-dark);
    background:linear-gradient(#ffa21a,#f07a00);font-size:14.5px;color:#1a1a1a;text-align:center;line-height:34px}

  /* promo banners */
  .promo{top:883px;height:77px}
  .promo-engage{left:23px;width:463px;background:var(--banner-blue)}
  .promo-engage .photo{left:0;top:0;width:210px;height:77px;background:linear-gradient(90deg,#b07a5a,#7a5240 70%,var(--banner-blue))}
  .promo-engage span{left:214px;top:25px;font-size:20px;color:#fff;white-space:nowrap}
  .promo-connect{left:499px;width:277px;background:var(--banner-light)}
  .promo-connect .photo{left:0;top:0;width:130px;height:77px;background:linear-gradient(90deg,#e8d6c6,#c9a47e 70%,var(--banner-light))}
  .promo-connect span{left:136px;top:13px;font-size:14px;line-height:17px;color:var(--navy)}

  /* footer */
  .footer{left:0;top:973px;width:800px;height:183px;background:var(--footer-bg)}
  .f-brand{left:30px;top:1004px;display:flex;align-items:center;gap:9px}
  .f-brand .dot{width:36px;height:36px;border-radius:50%;background:var(--brand)}
  .f-brand .name{font-size:19px;color:var(--brand)}
  .f-stay{left:49px;top:1080px;font-size:17px;color:var(--blue-link)}
  .social{top:1109px;width:22px;height:22px;border-radius:3px;background:#555;border:2px solid #ddd}
  .col-head{top:1003px;font-size:17px;color:var(--blue-link);display:flex;align-items:center;gap:9px}
  .post{font-family:"Arimo",sans-serif;font-size:10.5px;line-height:13px;color:#333;width:175px}
  .post small{display:block;font-size:7.5px;color:var(--blue-link);margin-top:3px}
  .post small b{font-weight:400;color:#333}
  .contact{left:622px;top:1033px;font-family:"Arimo",sans-serif;font-size:10.5px;line-height:13px;color:var(--blue-link)}
  .signup{left:627px;top:1094px;font-size:19px;line-height:22px;color:var(--navy)}
  .signup span{color:var(--blue-link)}
  .footer-bar{left:0;top:1156px;width:800px;height:44px;background:var(--footer-bar)}
  .foot-nav{left:32px;top:1169px;display:flex}
  .foot-nav a{color:#fff;text-decoration:none;font-size:13px;margin-right:28px}
  .copy{right:14px;top:1171px;font-family:"Arimo",sans-serif;font-size:10px;color:#999}
</style>
</head>
<body>
  <!-- header -->
  <div class="abs nav-band"></div>
  <div class="abs brand-dot"></div>
  <div class="abs brand-name">TeamPool.net</div>
  <div class="abs brand-tag">Developing your club together</div>
  <nav class="abs main-nav">
    <a href="#">Home</a><a href="#">About</a><a href="#">Our services</a><a href="#">Club Types</a><a href="#">News</a><a href="#">Information</a><a href="#">Contact</a>
  </nav>

  <!-- hero -->
  <div class="abs hero-frame"></div>
  <div class="abs hero-photo" role="img" aria-label="Photo of a football resting on a grass pitch"></div>
  <div class="abs hero-ball" role="img" aria-label="Football on the grass"></div>
  <div class="abs hero-line1">We help your Raise funds</div>
  <div class="abs hero-line2">Developing your club togerher</div>
  <div class="abs f-notch"></div>
  <div class="abs feature f-fund"><h3>FUNDRAISING</h3><p>Our online platform allows you to raise funds to</p></div>
  <div class="abs feature f-admin"><h3>ADMIN</h3><p>Our online platform allows you to raise funds to</p></div>
  <div class="abs feature f-goods"><h3>GOODS &amp; SERVICES</h3><p>Our online platform allows you to raise funds to</p></div>

  <!-- intro -->
  <p class="abs intro intro-1">Our online platform allows you to raise funds to buy equipment and develop your club.</p>
  <p class="abs intro intro-2">Watch the 2 minute video below and you can register for <span class="free">FREE below!</span></p>
  <svg class="abs intro-arrow" width="36" height="36" viewBox="0 0 36 36" aria-hidden="true">
    <path d="M6 6 Q10 20 22 24" stroke="#1f6fb8" stroke-width="6" fill="none" stroke-linecap="round"/>
    <path d="M14 28 L30 30 L26 14 Z" fill="#1f6fb8"/>
  </svg>

  <!-- register -->
  <section class="abs register"></section>
  <div class="abs video"></div>
  <div class="abs video-still" role="img" aria-label="Video still: introduction explaining how the platform helps clubs raise funds, engage with their community and get value"></div>
  <div class="abs video-progress"></div>
  <div class="abs video-controls"></div>
  <div class="abs play"></div>
  <div class="abs time">0:00</div>

  <h2 class="abs form-title">Register here completely FREE!</h2>
  <div class="abs field" style="top:562px">First Name*</div>
  <div class="abs field" style="top:607px">Last Name*</div>
  <div class="abs field" style="top:656px">Club Name*</div>
  <div class="abs field" style="top:705px">Email*</div>
  <div class="abs field field-select" style="top:754px">Club Type*</div>
  <div class="abs help">Pick the type that describes your club best</div>
  <div class="abs cta">Register Your Club Now</div>

  <!-- promos -->
  <div class="abs promo promo-engage">
    <div class="abs photo" role="img" aria-label="Photo of a smiling young man"></div>
    <span class="abs">ENGAGE WITH YOUR CLUB</span>
  </div>
  <div class="abs promo promo-connect">
    <div class="abs photo" role="img" aria-label="Photo of fingers holding a coin"></div>
    <span class="abs">USE YOUR<br>CONNECTIONSTO<br>DEVELOPYOUR CLUB</span>
  </div>

  <!-- footer -->
  <footer class="abs footer"></footer>
  <div class="abs f-brand"><div class="dot"></div><div class="name">TeamPool.net</div></div>
  <div class="abs f-stay">Stay in Touch</div>
  <div class="abs social" style="left:49px"></div>
  <div class="abs social" style="left:86px"></div>
  <div class="abs social" style="left:122px"></div>
  <div class="abs social" style="left:159px"></div>
  <div class="abs social" style="left:196px"></div>

  <div class="abs col-head" style="left:255px">
    <svg width="12" height="10" aria-hidden="true"><rect x="0" y="1" width="12" height="8" rx="2" fill="#333"/></svg>Twiter Feed
  </div>
  <div class="abs post" style="left:256px;top:1034px">Fully functioning Beginner Strategy EA10 seconds agobyspektra<small>33 minutes ago <b>by lantrel</b></small></div>
  <div class="abs post" style="left:256px;top:1097px">Fully functioning Beginner Strategy EA10 seconds agobyspektra<small>33 minutes ago <b>by lantrel</b></small></div>

  <div class="abs col-head" style="left:440px">
    <svg width="12" height="11" aria-hidden="true"><path d="M0 0H12V8H4L1 11V8H0Z" fill="#333"/></svg>Testimonials
  </div>
  <div class="abs post" style="left:441px;top:1034px">Fully functioning Beginner Strategy EA10 seconds agobyspektra<small>33 minutes ago <b>by lantrel</b></small></div>
  <div class="abs post" style="left:441px;top:1099px">Fully functioning Beginner Strategy EA10 seconds agobyspektra<small>33 minutes ago <b>by lantrel</b></small></div>

  <div class="abs col-head" style="left:621px">
    <svg width="10" height="13" aria-hidden="true"><path d="M5 13C5 13 0 7 0 5A5 5 0 0 1 10 5C10 7 5 13 5 13Z" fill="#333"/><circle cx="5" cy="5" r="2" fill="#f1f1f1"/></svg>Contact Us
  </div>
  <div class="abs contact">48 Harbour Lane Sydney AUS<br>Phone: 1800 55501234</div>
  <div class="abs signup">Sign up for<br><span>free now!</span></div>

  <div class="abs footer-bar"></div>
  <nav class="abs foot-nav">
    <a href="#">Home</a><a href="#">About</a><a href="#">Our services</a><a href="#">Club Types</a><a href="#">News</a><a href="#">Information</a><a href="#">Contact</a>
  </nav>
  <div class="abs copy">© TeamPool.net All Rights Reserved.</div>
</body>
</html>
```